Cafe Business needs a business card design

I already have an ai logo I would like to use and color. I need someone to make a business card for me on adobe illustrator with it. Its for a cafe restaurant opening in Japan I would like to be able to change out the names, contact info, ect on my own from adobe illustrator.

Industry/Entity Type

Business

Contact Information for Business Card

Double sided with logo on one side and info on the other. Name, Tel, fax, email and west

```html
<!DOCTYPE html>
<html lang="en">
<head>
<meta charset="utf-8">
<title>Kumo Bean Cafe – Business Card</title>
<link rel="stylesheet" href="https://fonts.googleapis.com/css2?family=Arimo:wght@400;700&display=swap">
<style>
  :root {
    --backdrop: #e3e3e1;
    --card-light: #fbfbfa;
    --card-brown: #6f584b;
    --brand-brown: #4a3328;
    --ink: #5b4236;
    --white: #ffffff;
  }
  * { box-sizing: border-box; margin: 0; padding: 0; }
  html, body {
    width: 1200px;
    height: 816px;
    overflow: hidden;
    background: var(--backdrop);
  }
  .canvas {
    position: relative;
    width: 1200px;
    height: 816px;
    font-family: "Arimo", Arial, sans-serif;
  }
  .card {
    position: absolute;
    width: 346px;
    height: 622px;
    display: flex;
    flex-direction: column;
    align-items: center;
  }
  .card--front {
    left: 149px;
    top: 96px;
    background: var(--card-light);
    color: var(--ink);
  }
  .card--back {
    left: 702px;
    top: 91px;
    background: var(--card-brown);
    color: var(--white);
    justify-content: center;
    padding-bottom: 60px;
  }
  .brand-mark {
    width: 144px;
    height: 144px;
    background: var(--brand-brown);
  }
  .card--front .brand-mark { margin-top: 132px; }
  .brand-mark--back {
    width: 72px;
    height: 72px;
    background: var(--white);
  }
  .brand-name {
    font-weight: 700;
    font-size: 30px;
    letter-spacing: 0.5px;
    text-align: center;
    line-height: 1.1;
    margin-top: 24px;
    color: var(--brand-brown);
  }
  .card--back .brand-name {
    color: var(--white);
    font-size: 27px;
    margin-top: 20px;
  }
  .person-name {
    margin-top: 74px;
    font-size: 20px;
    font-weight: 400;
    letter-spacing: 0.3px;
    text-transform: uppercase;
  }
  .contact {
    margin-top: 64px;
    font-size: 17px;
    line-height: 36px;
    text-align: center;
    font-style: normal;
  }
  .contact__phone { margin-top: 6px; display: block; }
</style>
</head>
<body>
  <main class="canvas">
    <section class="card card--front" aria-label="Card front with contact details">
      <div class="brand-mark" aria-hidden="true"></div>
      <div class="brand-name">KUMO BEAN<br>CAFE</div>
      <p class="person-name">Daniel Moreau</p>
      <address class="contact">
        48 Harbor Lane, Riverton,<br>
        Eastfield, 210455 USA
        <span class="contact__phone">+44 2070 - 118 - 2946</span>
      </address>
    </section>

    <section class="card card--back" aria-label="Card back with brand name">
      <div class="brand-mark brand-mark--back" aria-hidden="true"></div>
      <div class="brand-name">KUMO BEAN<br>CAFE</div>
    </section>
  </main>
</body>
</html>
```